Wine label refresh

We are wanting to modify our Corran Estate label to include a picture on it.
I have attached the pictures below which we would like on the label. They are of the Corran Estate vineyard. I have also attached an example of another label with a picture on it that we like the style of.
Industry/Entity Type
Vineyard
Requirements
Must have
- The Corran Estate text must stay the same but can be moved down. It still needs to be the same size though.
Marlborough Sauvignon Blanc should remain in the same font and roughly the same size.
Wine of New Zealand also must stay but could potentially be moved.
Nice to have
- It would be nice if we could keep the KL logo on the front label but feel free to experiment with where this goes.

```html
<!DOCTYPE html>
<html lang="en">
<head>
<meta charset="utf-8">
<title>Corran Estate – Marlborough Sauvignon Blanc Label</title>
<link rel="stylesheet" href="https://fonts.googleapis.com/css2?family=Cormorant+SC:wght@500&family=Pinyon+Script&family=Lato:wght@300&display=swap">
<style>
  :root {
    --page: #ffffff;
    --label-edge: #9a9a9a;
    --gold-dark: #8a6a1c;
    --gold-mid: #c9a23e;
    --gold-light: #fbefb0;
    --ink: #1c1c1c;
    --script: #c8194f;
    --muted: #7d7d7d;
    --monogram-mark: #ededef;
    --sepia-light: #d9c4bf;
    --sepia-mid: #a4837b;
    --sepia-dark: #5e4540;
  }

  html, body {
    margin: 0;
    padding: 0;
    overflow: hidden;
  }

  body {
    width: 1200px;
    height: 848px;
    background: var(--page);
    position: relative;
  }

  .wine-label {
    position: absolute;
    left: 270px;
    top: 74px;
    width: 660px;
    height: 700px;
    box-sizing: border-box;
    background: var(--page);
    border: 2px solid var(--label-edge);
  }

  .gold-frame {
    position: absolute;
    inset: 16px;
    background: linear-gradient(135deg,
      var(--gold-dark) 0%,
      var(--gold-light) 18%,
      var(--gold-mid) 38%,
      var(--gold-light) 55%,
      var(--gold-dark) 75%,
      var(--gold-light) 90%,
      var(--gold-mid) 100%);
  }

  .label-panel {
    position: absolute;
    inset: 20px;
    background: var(--page);
    border: 1px solid var(--label-edge);
    overflow: hidden;
  }

  .vineyard-photo {
    position: absolute;
    left: 14px;
    right: 14px;
    top: 16px;
    height: 290px;
    border: 2px solid var(--sepia-dark);
    background: linear-gradient(180deg,
      var(--sepia-light) 0%,
      var(--sepia-light) 35%,
      var(--sepia-mid) 55%,
      var(--sepia-dark) 72%,
      var(--sepia-mid) 100%);
  }

  .monogram-mark {
    position: absolute;
    left: 50%;
    top: 340px;
    width: 190px;
    height: 190px;
    margin-left: -95px;
    border-radius: 50%;
    background: var(--monogram-mark);
  }

  .estate-name {
    position: absolute;
    left: 0;
    right: 0;
    top: 384px;
    margin: 0;
    text-align: center;
    font-family: "Cormorant SC", serif;
    font-weight: 500;
    font-size: 50px;
    letter-spacing: 3px;
    color: var(--ink);
  }

  .estate-name sup {
    font-size: 16px;
    color: var(--muted);
    vertical-align: 28px;
    margin-left: 2px;
  }

  .varietal {
    position: absolute;
    left: 0;
    right: 0;
    top: 446px;
    margin: 0;
    text-align: center;
    font-family: "Pinyon Script", cursive;
    font-weight: 400;
    font-size: 44px;
    line-height: 52px;
    color: var(--script);
  }

  .label-footer {
    position: absolute;
    left: 14px;
    right: 14px;
    bottom: 14px;
    display: flex;
    justify-content: space-between;
    font-family: "Lato", sans-serif;
    font-weight: 300;
    font-size: 20px;
    color: var(--muted);
  }
</style>
</head>
<body>
  <div class="wine-label">
    <div class="gold-frame">
      <div class="label-panel">
        <div class="vineyard-photo" role="img" aria-label="Sepia photograph of the Corran Estate vineyard with palm trees, a homestead and hills"></div>
        <div class="monogram-mark" role="img" aria-label="Faint KL monogram mark"></div>
        <h1 class="estate-name">Corran Estate<sup>®</sup></h1>
        <p class="varietal">Marlborough Sauvignon Blanc<br>2012</p>
        <div class="label-footer">
          <span class="volume">750ml</span>
          <span class="origin">NEW ZEALAND WINE</span>
          <span class="abv">13% alc/vol</span>
        </div>
      </div>
    </div>
  </div>
</body>
</html>
```